Golden Years Wellness Roadmap: This is my second book. The first was Eldercare Compass

I need a book cover design for: GOLDEN YEARS WELLNESS ROADMAP: A NO-EXPENSE METHOD FOR FINISHING YOUR LATER-LIFE MOSAIC WITH POOLED KVB CARE SCHEMES by Derek Holloway Neil Osgrove & Martin Quarles. This book is designed for business owners, CEO's, CFO's and Human Resources. The cover needs to be professional and focused on business. The purpose of this book is to educate business owners and their management about a zero cost retiree health plan. This is a first of it's kind solution that every business needs to learn about.

Target Market(s)

Business owners, CEO's, CFO's and Human Resources

Requirements
Nice to have
• I want the design to be clean and professional since it is focused on business executives

```html
<!DOCTYPE html>
<html lang="en">
<head>
<meta charset="utf-8">
<title>Golden Years Wellness Roadmap – Cover Spread</title>
<link rel="stylesheet" href="https://fonts.googleapis.com/css2?family=Cinzel:wght@600;700&family=Montserrat:wght@400;500;600&display=swap">
<style>
  :root {
    --page-bg: #e9ebee;
    --paper: #ffffff;
    --navy: #1c2f5e;
    --navy-deep: #14224a;
    --accent-blue: #3e8fd0;
    --ink-grey: #6b6f78;
    --rule-grey: #9aa3b5;
    --puzzle-light: #eef1f5;
    --puzzle-mid: #dde3ec;
  }
  * { box-sizing: border-box; margin: 0; padding: 0; }
  html, body { width: 837px; height: 1200px; overflow: hidden; }
  body {
    background: var(--page-bg);
    font-family: "Montserrat", Arial, sans-serif;
    position: relative;
  }
  .cover-spread {
    position: absolute;
    left: 20px; top: 346px;
    width: 797px; height: 508px;
    background: var(--paper);
    display: flex;
    box-shadow: 0 2px 10px rgba(0,0,0,0.12);
    overflow: hidden;
  }
  .back-cover, .spine, .front-cover { position: relative; height: 100%; }
  .back-cover { width: 345px; }
  .spine { width: 60px; border-left: 1px solid #e3e6ec; border-right: 1px solid #e3e6ec; }
  .front-cover { width: 392px; }

  .puzzle-texture {
    position: absolute;
    background: linear-gradient(160deg, var(--puzzle-light), var(--puzzle-mid));
    opacity: 0.8;
  }
  .back-cover .puzzle-texture { left: 0; top: 250px; width: 345px; height: 210px; }

  .back-copy {
    position: absolute; left: 34px; top: 40px; width: 280px;
    font-size: 8.4px; line-height: 1.55; color: var(--ink-grey);
    text-align: justify;
  }
  .back-copy p + p { margin-top: 9px; }

  .spine-text {
    position: absolute; left: 0; top: 22px; width: 60px; height: 430px;
    writing-mode: vertical-rl;
    display: flex; flex-direction: row; align-items: center; justify-content: flex-start;
    gap: 8px;
  }
  .spine-title {
    font-family: "Cinzel", Georgia, serif; font-weight: 700;
    font-size: 17px; letter-spacing: 1px; color: var(--navy);
  }
  .spine-authors {
    font-size: 9px; font-weight: 600; letter-spacing: 0.5px; color: var(--navy);
  }

  .cover-art {
    position: absolute; left: 90px; top: 0; width: 212px; height: 175px;
    background: radial-gradient(circle at 50% 60%, #cfd9e6 0%, #e6ebf2 60%, #f4f6f9 100%);
  }
  .cover-title {
    position: absolute; left: 0; top: 192px; width: 392px; text-align: center;
    font-family: "Cinzel", Georgia, serif; color: var(--navy);
  }
  .cover-title .title-top { display: block; font-size: 22px; font-weight: 700; letter-spacing: 1px; }
  .cover-title .title-main { display: block; font-size: 44px; font-weight: 700; letter-spacing: 2px; line-height: 1.1; }
  .cover-subtitle {
    position: absolute; left: 40px; top: 292px; width: 312px; text-align: center;
    font-size: 8.6px; font-weight: 600; letter-spacing: 1px; line-height: 1.6;
    color: var(--navy);
    border-top: 1px solid var(--rule-grey); padding-top: 8px;
  }
  .cover-subtitle .lead { font-size: 9.4px; }
  .front-cover .puzzle-texture { left: 0; top: 355px; width: 392px; height: 95px; opacity: 0.5; }
  .cover-authors {
    position: absolute; left: 0; top: 452px; width: 392px; text-align: center;
    font-size: 9.5px; font-weight: 600; letter-spacing: 1px; color: var(--navy);
  }
  .bottom-band {
    position: absolute; left: 0; bottom: 0; width: 797px; height: 30px;
    background: var(--navy-deep);
    border-top: 3px solid var(--accent-blue);
  }
</style>
</head>
<body>
  <main class="cover-spread">
    <section class="back-cover">
      <div class="back-copy">
        <p>Retiree health costs rise every year, and most firms carry that burden with no clear plan. This book shows owners and finance leaders a new way to fund retiree care without adding cost to the company. Step by step, the authors explain how pooled plans work, who qualifies, and how to put one in place.</p>
        <p>Written for CEOs, CFOs and human resources teams, it turns a complex topic into plain language and practical checklists.</p>
      </div>
      <div class="puzzle-texture" role="img" aria-label="Faint interlocking puzzle-piece pattern"></div>
    </section>

    <section class="spine">
      <div class="spine-text">
        <span class="spine-title">GOLDEN YEARS WELLNESS ROADMAP</span>
        <span class="spine-authors">DEREK HOLLOWAY · NEIL OSGROVE &amp; MARTIN QUARLES</span>
      </div>
    </section>

    <section class="front-cover">
      <div class="cover-art" role="img" aria-label="Hand placing a puzzle piece bearing a medical staff symbol"></div>
      <h1 class="cover-title">
        <span class="title-top">GOLDEN YEARS WELLNESS</span>
        <span class="title-main">ROADMAP</span>
      </h1>
      <p class="cover-subtitle">
        <span class="lead">A NO-EXPENSE METHOD FOR FINISHING</span><br>
        YOUR LATER-LIFE MOSAIC WITH<br>
        POOLED KVB CARE SCHEMES
      </p>
      <div class="puzzle-texture" role="img" aria-label="Faint interlocking puzzle-piece pattern"></div>
      <p class="cover-authors">DEREK HOLLOWAY · NEIL OSGROVE &amp; MARTIN QUARLES</p>
    </section>

    <div class="bottom-band"></div>
  </main>
</body>
</html>
```